Rogue Zinfandel wine label

I need a wine label designed for a new wine brand. I am open to anything, but I think the simpler and bolder the better so it will stand out on the shelf amongst the hundreds of brands out there.
Label should have the word ROGUE buy itself with the word Zinfandel under it.

```html
<!DOCTYPE html>
<html lang="en">
<head>
<meta charset="utf-8">
<title>Rogue Zinfandel – Wine Label</title>
<link href="https://fonts.googleapis.com/css2?family=Pacifico&display=swap" rel="stylesheet">
<style>
  :root {
    --bg-centre: #ffffff;
    --bg-edge: #d8d8d9;
    --label-rim: #58585a;
    --label-line: #ffffff;
    --label-fill-light: #8e8e90;
    --label-fill-dark: #5c5c5e;
    --label-text: #f2f2f2;
    --pattern-tone: #58585a;
  }
  html, body {
    margin: 0;
    padding: 0;
    width: 1200px;
    height: 927px;
    overflow: hidden;
  }
  .canvas {
    position: relative;
    width: 1200px;
    height: 927px;
    background: radial-gradient(ellipse at 50% 45%, var(--bg-centre) 0%, var(--bg-edge) 100%);
  }
  .front-label {
    position: absolute;
    left: 0;
    top: 0;
  }
  .label-rim { fill: var(--label-rim); }
  .label-line { fill: none; stroke: var(--label-line); stroke-width: 5; }
  .brand-name {
    font-family: "Pacifico", "Brush Script MT", "Segoe Script", cursive;
    font-weight: 700;
    font-size: 84px;
    fill: var(--label-text);
  }
  .varietal {
    font-family: "Pacifico", "Brush Script MT", "Segoe Script", cursive;
    font-weight: 700;
    font-size: 30px;
    fill: var(--label-text);
  }
  .neck-pattern {
    position: absolute;
    left: 182px;
    top: 620px;
    width: 434px;
    height: 190px;
    background: var(--pattern-tone);
  }
</style>
</head>
<body>
<main class="canvas">
  <svg class="front-label" width="800" height="600" viewBox="0 0 800 600" aria-label="Rogue Zinfandel front label">
    <defs>
      <path id="label-shape" d="M400,45 Q380,140 262,152 Q250,280 115,298 Q250,318 262,448 Q380,458 400,555 Q420,458 538,448 Q550,318 685,298 Q550,280 538,152 Q420,140 400,45 Z"/>
      <radialGradient id="label-fill" cx="50%" cy="50%" r="55%">
        <stop offset="0%" stop-color="var(--label-fill-light)"/>
        <stop offset="100%" stop-color="var(--label-fill-dark)"/>
      </radialGradient>
    </defs>
    <use href="#label-shape" class="label-rim" stroke="var(--label-rim)" stroke-width="12" stroke-linejoin="round"/>
    <use href="#label-shape" class="label-line" transform="translate(400 300) scale(0.95) translate(-400 -300)" stroke-linejoin="round"/>
    <use href="#label-shape" fill="url(#label-fill)" transform="translate(400 300) scale(0.925) translate(-400 -300)" stroke-linejoin="round"/>
    <g transform="rotate(-5 400 300)">
      <text class="brand-name" x="250" y="312" textLength="300" lengthAdjust="spacingAndGlyphs">Rogue</text>
      <text class="varietal" x="372" y="378" textLength="165" lengthAdjust="spacingAndGlyphs">Zinfandel</text>
    </g>
  </svg>
  <div class="neck-pattern" role="img" aria-label="Grey quatrefoil lattice pattern for the neck band"></div>
</main>
</body>
</html>
```